Quellmoor Imaging

I wish to make a mailing of a postcard format to pathologists in the UK. Probable number between 500 and 1000.There are 3 elements. 1. A small number of words (about 12) 2. A picture of our product 3. A relevant (tissue section) background. I have knocked up a rough idea of what I want ... BUT ... I'm obviously not a designer. The text looks awful and needs some way of standing out (and being legible) against the background. I can send original images of product and background. Important ... Aspect ratios of images must not be changed.
Look and feel
Each slider illustrates characteristics of the customer's brand and the style your logo design should communicate.

```html
<!DOCTYPE html>
<html lang="en">
<head>
<meta charset="utf-8">
<title>Quellmoor Imaging – Whole Slide Scanning</title>
<link rel="stylesheet" href="https://fonts.googleapis.com/css2?family=Montserrat:ital,wght@0,700;0,800;1,800&display=swap">
<style>
  :root {
    --paper: #ffffff;
    --headline: #7a2f6c;
    --ink: #141414;
    --tissue-deep: #a8437f;
    --tissue-mid: #c977a8;
    --tissue-light: #e7c2d8;
    --band-dark: #6d5868;
    --band-light: #d9d0d8;
    --device-light: #f4f4f4;
    --device-shade: #bdbdbd;
  }
  html, body {
    margin: 0;
    padding: 0;
    width: 929px;
    height: 1200px;
    overflow: hidden;
    background: var(--paper);
  }
  .postcard {
    position: relative;
    width: 929px;
    height: 1200px;
    background: var(--paper);
    font-family: "Montserrat", Arial, sans-serif;
    overflow: hidden;
  }
  .headline {
    position: absolute;
    left: 0;
    right: 0;
    top: 32px;
    margin: 0;
    text-align: center;
    font-size: 52px;
    font-style: italic;
    font-weight: 800;
    color: var(--headline);
    letter-spacing: -0.5px;
  }
  .benefits {
    position: absolute;
    left: 70px;
    top: 150px;
    width: 840px;
    margin: 0;
    padding: 0;
    list-style: none;
    display: grid;
    grid-template-columns: 383px 457px;
    row-gap: 4px;
  }
  .benefits li {
    font-size: 62px;
    font-weight: 800;
    color: var(--ink);
    line-height: 82px;
    letter-spacing: -0.5px;
    white-space: nowrap;
  }
  .benefits li::before {
    content: "\2022";
    margin-right: 20px;
  }
  .artwork {
    position: absolute;
    left: 0;
    top: 0;
  }
  .brand {
    position: absolute;
    left: 0;
    right: 0;
    top: 1098px;
    display: flex;
    justify-content: center;
    align-items: center;
    gap: 14px;
  }
  .brand-dot {
    width: 38px;
    height: 38px;
    border-radius: 50%;
    background: var(--ink);
  }
  .brand-name {
    font-size: 30px;
    font-weight: 700;
    color: var(--ink);
    line-height: 32px;
  }
</style>
</head>
<body>
<main class="postcard">
  <svg class="artwork" width="929" height="1200" viewBox="0 0 929 1200">
    <defs>
      <linearGradient id="tissueTone" x1="0" y1="0" x2="1" y2="1">
        <stop offset="0" stop-color="var(--tissue-light)"/>
        <stop offset="0.45" stop-color="var(--tissue-mid)"/>
        <stop offset="1" stop-color="var(--tissue-deep)"/>
      </linearGradient>
      <linearGradient id="bandTone" x1="0" y1="0" x2="1" y2="0">
        <stop offset="0" stop-color="var(--band-dark)"/>
        <stop offset="0.5" stop-color="var(--band-light)"/>
        <stop offset="1" stop-color="var(--band-dark)"/>
      </linearGradient>
      <linearGradient id="deviceTone" x1="0" y1="0" x2="1" y2="1">
        <stop offset="0" stop-color="var(--device-light)"/>
        <stop offset="1" stop-color="var(--device-shade)"/>
      </linearGradient>
    </defs>
    <polygon class="top-band" points="0,520 464,650 929,520 929,566 464,694 0,566" fill="url(#bandTone)"/>
    <polygon class="tissue-section" role="img" aria-label="Stained tissue section micrograph in pink and purple"
      points="0,566 464,694 929,566 929,1150 464,1050 0,1150" fill="url(#tissueTone)"/>
    <polygon class="bottom-band" points="0,1136 464,1036 929,1136 929,1156 464,1062 0,1156" fill="url(#bandTone)"/>
    <polygon class="bottom-panel" points="0,1156 464,1062 929,1156 929,1200 0,1200" fill="var(--paper)"/>
    <rect class="product-photo" role="img" aria-label="Photo of the compact white whole slide scanner"
      x="215" y="352" width="485" height="465" rx="40" fill="url(#deviceTone)"/>
  </svg>

  <h1 class="headline">Whole Slide Scanning is now ...</h1>
  <ul class="benefits">
    <li>Compact</li>
    <li>Simple</li>
    <li>Fast</li>
    <li>Affordable</li>
  </ul>

  <div class="brand">
    <span class="brand-dot"></span>
    <span class="brand-name">Quellmoor<br>Imaging</span>
  </div>
</main>
</body>
</html>
```